bold, classy, clean design for legal stationary and business cards - more modern than traditional
New law office stationary, that looks like the firm is bold, successful, professional, and not new.
bold, classy, clean design for legal stationary and business cards - more modern than traditional - Law
Creative Brief
Professional
Tess R. Ford
Law Office of Tess R. Ford, LLC 47 W. Harlow Avenue, Suite 315 Chicago, IL 60699
Office - 312-555-0148
Mobile - 773-555-0172
trf@tessfordcounsel.example
www.tessfordcounsel.example
I have purchased a logo, and I hope that I attach the correct format. I am a new company, so I am trying to be cost conscious, yet have the card look like a million bucks. The logo is red and dark grey. I would like to keep the card to just those colors, and only have red on the front, I hope that saves money. If you think the type should be black rather than dark grey, I am OK with that. The back side (I think) should just be black or dark grey. I would like something professional and bold.
I would like these four areas of practice on the back of the card: personal injury wrongful death medical malpractice auto accidents perhaps putting a dash/diamond/line in-between the words
tessfordcounsel tessfordcounsel
Can you please show me stationary designs for letterhead and envelopes.

```html
<!DOCTYPE html>
<html lang="en">
<head>
<meta charset="utf-8">
<title>Law Office of Tess R. Ford — Stationery Set</title>
<link rel="stylesheet" href="https://fonts.googleapis.com/css2?family=Cinzel:wght@400&family=Open+Sans:wght@400;600&display=swap">
<style>
  :root {
    --backdrop: #a4a4a4;
    --paper: #ffffff;
    --ink: #3b3b3d;
    --ink-soft: #6d6d70;
    --charcoal: #4a4a4c;
    --red: #c8202f;
    --rule: #c9c9cb;
    --shadow: 0 2px 6px rgba(0,0,0,.25);
  }
  * { box-sizing: border-box; margin: 0; padding: 0; }
  html, body { width: 1200px; height: 838px; overflow: hidden; }
  body {
    background: var(--backdrop);
    font-family: "Open Sans", Arial, sans-serif;
    color: var(--ink);
    position: relative;
  }
  .piece { position: absolute; box-shadow: var(--shadow); background: var(--paper); }

  /* Brand lockup: plain square + firm name in one colour and weight */
  .lockup { display: flex; align-items: center; gap: 6px; }
  .lockup-mark { background: var(--red); flex: none; }
  .lockup-name {
    font-family: "Cinzel", Georgia, serif;
    font-weight: 400;
    color: var(--ink);
    line-height: 1.1;
    letter-spacing: .04em;
  }

  .contact-list { list-style: none; }
  .contact-list li { display: flex; align-items: center; gap: 4px; white-space: nowrap; }
  .contact-list li::before {
    content: ""; width: 4px; height: 4px; background: var(--red); flex: none;
  }

  /* Business card back */
  .card-back {
    left: 144px; top: 91px; width: 236px; height: 130px;
    background: var(--charcoal);
    display: flex; align-items: center; justify-content: space-between;
    padding: 0 20px;
  }
  .card-back .lockup-mark { width: 22px; height: 22px; }
  .card-back .lockup-name { color: var(--paper); font-size: 8px; width: 82px; }
  .practice-box {
    border: 1px solid var(--paper);
    color: var(--paper);
    font-size: 5.5px; line-height: 1.6;
    padding: 5px 7px; text-align: center; letter-spacing: .06em; text-transform: uppercase;
  }

  /* Business card front */
  .card-front { left: 397px; top: 91px; width: 204px; height: 130px; }
  .card-front .lockup { position: absolute; left: 72px; top: 14px; }
  .card-front .lockup-mark { width: 20px; height: 20px; }
  .card-front .lockup-name { font-size: 7.5px; width: 100px; }
  .card-front .card-name {
    position: absolute; left: 12px; top: 62px;
    font-family: "Cinzel", Georgia, serif; font-size: 8px; letter-spacing: .05em;
  }
  .card-front .card-address { position: absolute; left: 72px; top: 52px; font-size: 4.5px; line-height: 1.5; }
  .card-front .contact-list { position: absolute; left: 72px; top: 70px; font-size: 4.5px; line-height: 1.6; }

  /* Envelope front */
  .envelope-front { left: 113px; top: 295px; width: 488px; height: 281px; }
  .envelope-front .lockup { position: absolute; left: 20px; top: 26px; gap: 8px; }
  .envelope-front .lockup-mark { width: 30px; height: 30px; }
  .envelope-front .lockup-name { font-size: 10px; width: 130px; }
  .envelope-front .return {
    position: absolute; left: 20px; top: 150px; display: flex; gap: 10px; align-items: stretch;
  }
  .return-address { font-size: 6px; line-height: 1.6; text-transform: uppercase; letter-spacing: .04em; }
  .return-divider { width: 1px; background: var(--rule); }
  .return .contact-list { font-size: 5.5px; line-height: 1.7; }

  /* Envelope back */
  .envelope-back { left: 113px; top: 617px; width: 488px; height: 151px; }
  .envelope-back svg { position: absolute; inset: 0; }
  .envelope-back .lockup { position: absolute; left: 172px; top: 28px; gap: 8px; }
  .envelope-back .lockup-mark { width: 28px; height: 28px; }
  .envelope-back .lockup-name { color: var(--paper); font-size: 10px; width: 130px; }

  /* Letterhead */
  .letterhead { left: 619px; top: 96px; width: 456px; height: 667px; padding: 0 38px; }
  .letterhead .lockup { position: absolute; left: 38px; top: 34px; gap: 8px; }
  .letterhead .lockup-mark { width: 30px; height: 30px; }
  .letterhead .lockup-name { font-size: 10px; width: 140px; }
  .letter-body { position: absolute; left: 38px; right: 38px; top: 116px; font-size: 6.5px; line-height: 1.75; color: var(--ink-soft); }
  .recipient { margin-bottom: 16px; color: var(--ink); }
  .recipient strong { font-weight: 600; letter-spacing: .05em; }
  .letter-body p { margin-bottom: 12px; text-align: justify; }
  .signature {
    position: absolute; right: 56px; top: 515px; width: 70px; height: 34px;
    background: linear-gradient(90deg, rgba(59,59,61,.08), rgba(59,59,61,.22), rgba(59,59,61,.08));
    border-radius: 14px;
  }
  .signer { position: absolute; right: 56px; top: 556px; font-size: 5.5px; color: var(--ink); }
  .letter-footer {
    position: absolute; left: 38px; bottom: 30px; display: flex; gap: 10px; align-items: stretch;
  }
</style>
</head>
<body>

  <section class="piece card-back" aria-label="Business card, back">
    <div class="lockup">
      <span class="lockup-mark"></span>
      <span class="lockup-name">Law Office of Tess R. Ford</span>
    </div>
    <div class="practice-box">
      Personal Injury<br>Wrongful Death<br>Medical Malpractice<br>Auto Accidents
    </div>
  </section>

  <section class="piece card-front" aria-label="Business card, front">
    <div class="lockup">
      <span class="lockup-mark"></span>
      <span class="lockup-name">Law Office of Tess R. Ford</span>
    </div>
    <div class="card-name">Tess R. Ford</div>
    <div class="card-address">47 W. Harlow Avenue, Suite 315<br>Chicago, IL 60699</div>
    <ul class="contact-list">
      <li>312-555-0148</li>
      <li>773-555-0172</li>
      <li>trf@tessfordcounsel.example</li>
      <li>www.tessfordcounsel.example</li>
    </ul>
  </section>

  <section class="piece envelope-front" aria-label="Envelope, front">
    <div class="lockup">
      <span class="lockup-mark"></span>
      <span class="lockup-name">Law Office of Tess R. Ford</span>
    </div>
    <div class="return">
      <div class="return-address">47 W. Harlow Avenue, Suite 315<br>Chicago, IL 60699</div>
      <span class="return-divider"></span>
      <ul class="contact-list">
        <li>312-555-0148</li>
        <li>773-555-0172</li>
        <li>trf@tessfordcounsel.example</li>
        <li>www.tessfordcounsel.example</li>
      </ul>
    </div>
  </section>

  <section class="piece envelope-back" aria-label="Envelope, back">
    <svg width="488" height="151" viewBox="0 0 488 151">
      <polygon points="0,0 488,0 488,20 244,120 0,20" fill="var(--charcoal)"/>
    </svg>
    <div class="lockup">
      <span class="lockup-mark"></span>
      <span class="lockup-name">Law Office of Tess R. Ford</span>
    </div>
  </section>

  <section class="piece letterhead" aria-label="Letterhead">
    <div class="lockup">
      <span class="lockup-mark"></span>
      <span class="lockup-name">Law Office of Tess R. Ford</span>
    </div>
    <div class="letter-body">
      <div class="recipient">
        <strong>CLIENT NAME HERE</strong><br>
        12 Sample Road, Suite 4B<br>
        Springfield Area, IL 60000<br>
        Re: Matter reference 2041
      </div>
      <p>Dear Client,</p>
      <p>Thank you for meeting with our office this week. This letter confirms the scope of our engagement and the next steps we discussed together. We will review the records you provided, contact the parties involved, and prepare a written summary of your options. Please keep copies of any new documents you receive.</p>
      <p>Our team will remain in regular contact as the matter moves forward. If questions arise at any point, call the office directly and we will respond promptly. Timelines can change, so we will send updates whenever a date or filing is confirmed.</p>
      <p>We appreciate the trust you have placed in us and look forward to working with you.</p>
    </div>
    <div class="signature" role="img" aria-label="Handwritten signature"></div>
    <div class="signer">Tess R. Ford</div>
    <div class="letter-footer">
      <div class="return-address">47 W. Harlow Avenue, Suite 315<br>Chicago, IL 60699</div>
      <span class="return-divider"></span>
      <ul class="contact-list" style="font-size:5.5px;line-height:1.7">
        <li>312-555-0148</li>
        <li>773-555-0172</li>
        <li>trf@tessfordcounsel.example</li>
        <li>www.tessfordcounsel.example</li>
      </ul>
    </div>
  </section>

</body>
</html>
```